Marnie Lux Business Card Design

I need a business card for my daughter. She has it all described in the file below. But it needs to be square in shape. http://www.marnielux.com is her web site

Target Market(s)

18-35 year old women

Industry/Entity Type

Fashion

Contact Information for Business Card

Please look at the attached file as it has all the details.

Requirements
Must have
• Please look at the attached file as it has all the details.
Nice to have
Should not have

```html
<!DOCTYPE html>
<html lang="en">
<head>
<meta charset="utf-8">
<title>Marnie Lux Business Card</title>
<link rel="stylesheet" href="https://fonts.googleapis.com/css2?family=Abril+Fatface&family=Kalam:wght@400&family=Roboto:wght@400;700&display=swap">
<style>
  :root {
    --pink: #f6c4dc;
    --ink: #000000;
    --white: #ffffff;
    --olive: #3b3a2c;
    --page: #ffffff;
    --shadow: rgba(0, 0, 0, 0.28);
  }
  * { margin: 0; padding: 0; box-sizing: border-box; }
  html, body {
    width: 1200px; height: 1000px; overflow: hidden;
    background: var(--page);
  }
  .canvas { position: relative; width: 1200px; height: 1000px; }

  .card {
    position: absolute; top: 271px;
    width: 458px; height: 458px;
    background: var(--pink);
    box-shadow: 1px 2px 4px var(--shadow);
  }
  .card--front { left: 98px; }
  .card--back { left: 616px; }

  .card__panel {
    position: absolute; left: 12px; top: 13px;
    width: 433px; height: 432px;
    background: var(--ink);
  }
  .card__texture {
    position: absolute; inset: 0;
    background: radial-gradient(ellipse at 40% 40%, #2a2920 0%, #1a1914 55%, #0d0d0a 100%);
  }

  .brand {
    position: absolute; left: 0; right: 0; top: 166px;
    text-align: center;
  }
  .brand__name {
    font-family: "Abril Fatface", serif;
    font-size: 43px; letter-spacing: 2px;
    color: var(--pink); line-height: 1;
  }
  .brand__rule {
    width: 228px; height: 1px; margin: 10px auto 0;
    background: var(--white);
  }
  .brand__tagline {
    font-family: "Kalam", cursive;
    font-size: 22px; color: var(--pink);
    margin-top: 4px; letter-spacing: 0.5px;
  }

  .roles {
    position: absolute; left: 21px; top: 20px;
    width: 391px; height: 35px;
    background: var(--pink);
    font-family: "Kalam", cursive; font-size: 16px;
    color: var(--white); text-align: center; line-height: 35px;
    letter-spacing: 0.3px;
  }

  .contacts { position: absolute; left: 21px; top: 91px; list-style: none; }
  .contacts__item {
    display: flex; align-items: center;
    height: 32px; margin-bottom: 13.5px;
    font-family: "Roboto", sans-serif; font-weight: 700;
    font-size: 24px; color: var(--white);
  }
  .contacts__icon {
    width: 32px; height: 32px; margin-right: 19px; flex: none;
  }

  .links { position: absolute; left: 21px; top: 322px; }
  .links__row {
    font-family: "Roboto", sans-serif; font-size: 22px;
    color: var(--white); line-height: 36px; white-space: nowrap;
  }
  .links__label {
    font-family: "Abril Fatface", serif;
    color: var(--pink); letter-spacing: 1px;
  }
</style>
</head>
<body>
<div class="canvas">

  <section class="card card--front">
    <div class="card__panel">
      <div class="card__texture" role="img" aria-label="Dark olive ink splatter texture across a black background"></div>
      <div class="brand">
        <h1 class="brand__name">MARNIE LUX</h1>
        <div class="brand__rule"></div>
        <p class="brand__tagline">let's talk fashion</p>
      </div>
    </div>
  </section>

  <section class="card card--back">
    <div class="card__panel">
      <p class="roles">blogger &amp; vlogger//beauty-fashion-travel</p>

      <ul class="contacts">
        <li class="contacts__item">
          <svg class="contacts__icon" viewBox="0 0 32 32"><circle cx="16" cy="16" r="16" fill="var(--pink)"/></svg>
          photoreel.com/marnieluxxo
        </li>
        <li class="contacts__item">
          <svg class="contacts__icon" viewBox="0 0 32 32"><circle cx="16" cy="16" r="16" fill="var(--pink)"/></svg>
          chirpline.com/marnieluxxo
        </li>
        <li class="contacts__item">
          <svg class="contacts__icon" viewBox="0 0 32 32"><circle cx="16" cy="16" r="16" fill="var(--pink)"/></svg>
          @marnieluxxo
        </li>
        <li class="contacts__item">
          <svg class="contacts__icon" viewBox="0 0 32 32">
            <circle cx="16" cy="16" r="16" fill="var(--pink)"/>
            <rect x="8.5" y="10.5" width="15" height="11" fill="none" stroke="var(--white)" stroke-width="1.6"/>
            <polyline points="8.5,10.5 16,17 23.5,10.5" fill="none" stroke="var(--white)" stroke-width="1.6"/>
          </svg>
          marnie@marnielux.com
        </li>
      </ul>

      <div class="links">
        <p class="links__row"><span class="links__label">BLOG:</span> marnielux.com</p>
        <p class="links__row"><span class="links__label">VIDSTREAM:</span> vidstream.com/marnielux</p>
      </div>
    </div>
  </section>

</div>
</body>
</html>
```